Wine Label front and back- Need to have an eye catching, classy wine label for restaurant placement.

label design for a wine label. eye catching for shelf placement. looking for simple and elegant label. Name of the vineyard will be the label recognition. Need back label to match with coloring and basic regulated info required by gov't (producer, address, and statement) Back label will be addressed after selected front label to match.
Will add $100 extra for the back label to match.

Target Market(s)

40-65 year old foodies

Colors
0355a3
eaf1f7

Requirements
Must have
• FERNHOLLOW (label name)
Estate,
Red Wine Blend NV,

```html
<!DOCTYPE html>
<html lang="en">
<head>
<meta charset="utf-8">
<title>Fernhollow Estate Label</title>
<link rel="stylesheet" href="https://fonts.googleapis.com/css2?family=EB+Garamond:wght@400;500&display=swap">
<style>
  :root {
    --backdrop: #d3bb94;
    --label-paper: #dde4ec;
    --brand-blue: #0355a3;
    --ink-grey: #5b5f66;
    --rule-grey: #8a8f96;
    --photo-light: #d9d2c3;
    --photo-mid: #8c7f6c;
    --photo-dark: #3f362c;
  }
  * { margin: 0; padding: 0; box-sizing: border-box; }
  html, body {
    width: 1200px;
    height: 864px;
    overflow: hidden;
    background: var(--backdrop);
  }
  .canvas {
    width: 1200px;
    height: 864px;
    display: flex;
    align-items: center;
    justify-content: center;
  }
  .front-label {
    width: 560px;
    height: 760px;
    background: var(--label-paper);
    display: flex;
    flex-direction: column;
    align-items: center;
    padding-top: 48px;
    font-family: "EB Garamond", Georgia, serif;
    text-align: center;
  }
  .vineyard-photo {
    width: 420px;
    height: 360px;
    background:
      linear-gradient(180deg, var(--photo-light) 0%, var(--photo-light) 18%, var(--photo-mid) 34%, var(--photo-dark) 70%, var(--photo-mid) 100%);
  }
  .brand-name {
    margin-top: 40px;
    color: var(--brand-blue);
    font-size: 36px;
    font-weight: 500;
    letter-spacing: 0.28em;
    padding-left: 0.28em;
  }
  .divider {
    width: 380px;
    height: 1px;
    background: var(--rule-grey);
    margin: 16px 0 18px;
  }
  .origin {
    color: var(--ink-grey);
    font-size: 19px;
    letter-spacing: 0.14em;
    line-height: 1.2;
  }
  .style {
    margin-top: 26px;
    color: var(--ink-grey);
    font-size: 19px;
    letter-spacing: 0.12em;
    line-height: 1.4;
  }
  .volume {
    margin-top: 22px;
    color: var(--brand-blue);
    font-size: 17px;
    letter-spacing: 0.04em;
  }
</style>
</head>
<body>
  <main class="canvas">
    <section class="front-label">
      <div class="vineyard-photo" role="img" aria-label="Sepia photograph of vineyard rows sweeping toward distant hills"></div>
      <h1 class="brand-name">FERNHOLLOW</h1>
      <div class="divider"></div>
      <p class="origin">GROWN AND BOTTLED IN<br>FERNHOLLOW</p>
      <p class="style">Estate<br>Red Wine Blend NV</p>
      <p class="volume">750 mls</p>
    </section>
  </main>
</body>
</html>
```